Label Design for RTD Cocktail Line Tovelin Spirits

Tovelin Spirits is a line of Indian-inspired artisan cocktails that "brings the bartender home" for professional men and women who like the finer things in life but don’t always have the time to treat themselves. No need for a multitude of expensive and hard-to-find ingredients, time consuming recipes, or a mixologist.

Our line of 3 open and serve cocktails blends a range of premium spirits with exotic ingredients so you can conveniently raise a glass for any of life’s celebrations.

Our bottle is the 750ml Claret bottle with Quarnet (screw cap) closure and will be covered entirely in a shrink sleeve (so potentially anything can be designed for any part of the bottle). We want the bottle to pop on the shelf so it should look different than what’s already out there (Velvet Moth, Galdrova, Merlusa ready to drink cocktails). We are looking for a sexy design that's polished/sleek.
Updates

Project Deadline Extended
Reason: Hello designers! Tovelin Spirits is so impressed with what we have received thus far and we would like to give some of the designers a few extra days to make the edits we requested. It's never too late to submit! Thank you all!

Industry/Entity Type

It Professional

Requirements
Must have
• Front of bottle
* “Tovelin Spirits” name and Peacock Logo- but feel free to pull the elements apart and use them on the bottle in different ways
* Open & Serve
* 12% ALC/VOL
* 750 ml
* 3 different labels in a theme for
-Borvelle
-Faluntera
-Pomadrine

Borvelle Ideas- soft brown palate, the ingredients in chai spice (cloves, cardamom pods, nutmeg, black peppercorns, star anise, and cinnamon stick)

Faluntera Ideas -cool and refreshing, pale green shade (not clashing with logo), graphics of fresh mint leaves, green chili, lime, cucumber

Pomadrine Ideas- soft/pale pink shades, graphics of lychi fruit (outer red shell and inner pink flesh), ginger

Back of bottle
* explanation of the 3 cocktails
Borvelle: Forget what you think you know about chai, this is not the Queen’s tea-time drink! Borvelle is a smooth, sweetly -spiced cocktail made with vodka, black tea, and a combination of aromatic spices. This velvety cocktail is rich without being heavy. Enjoy chilled or over ice anytime.

Faluntera: Faluntera can’t make up its mind! This fusion of zesty lime, sweet mint, earthy cucumber and spicy chilies is so refreshing you’ll crave it on a hot summer day or a cool winter’s night. The exotic botanicals in gin add a complexity to the cocktail making this a refreshing but potent drink! Enjoy chilled or over ice anytime.

Pomadrine: East meet West. Delicate lychi meet hard-hitting whiskey. Pomadrine will tempt you senses with flavor, fragrance and beauty. The peppery kick of ginger and the intensity of the un-aged whiskey are softened by lychi’s intoxicating scent and subtle, sweet finish.

Please include
1. Bottled By QRW Spirits Company
2. Sample barcode (where you would place it in your design)
3. www.TovelinSpirits.example
4. GOVERNMENT WARNING: (1) According to the Surgeon General, women should not drink alcoholic beverages during pregnancy because of the risk of birth defects. (2) Consumption of alcoholic beverages impairs your ability to drive a car or operate machinery, and may cause health problems.

Optional to include
*"Bring the Bartender Home"
*"Tovelin Spirits” name and Peacock Logo on the back
*Entirely black sleeve with contrasting design

FYI the Fonts used in our logo are Geosans Light and Prakrta, but feel free to use other complimentary fonts on the other aspects.
Nice to have
• Optional to include

```html
<!DOCTYPE html>
<html lang="en">
<head>
<meta charset="utf-8">
<title>Tovelin Spirits – Cocktail Labels</title>
<link rel="stylesheet" href="https://fonts.googleapis.com/css2?family=Roboto:wght@300;400&display=swap">
<style>
  :root {
    --canvas: #ececec;
    --ink: #1e1e1e;
    --ink-soft: #4a4a4a;
    --chai-fill: #dcc39e;
    --chai-edge: #8b6448;
    --chai-rim: #b08a66;
    --chai-spice-a: #7a4424;
    --chai-spice-b: #a86c42;
    --mint-fill: #abd46c;
    --mint-edge: #2f9a48;
    --mint-rim: #6dbb52;
    --mint-leaf-a: #3f8f2f;
    --mint-leaf-b: #8cc84a;
    --lychee-fill: #ecb9d6;
    --lychee-edge: #cf2f86;
    --lychee-rim: #e07ab3;
    --lychee-fruit-a: #c8564e;
    --lychee-fruit-b: #d99a3e;
  }
  * { margin: 0; padding: 0; box-sizing: border-box; }
  html, body { width: 1200px; height: 900px; overflow: hidden; }
  body {
    background: var(--canvas);
    font-family: "Roboto", Arial, sans-serif;
    color: var(--ink);
  }
  .label-set {
    position: relative;
    width: 1200px;
    height: 900px;
  }
  .label-unit {
    position: absolute;
    top: 264px;
    width: 210px;
  }
  .label-unit--chai { left: 214px; }
  .label-unit--mint { left: 510px; }
  .label-unit--lychee { left: 796px; }

  .label {
    position: relative;
    width: 210px;
    height: 236px;
  }
  .label__shape {
    position: absolute;
    inset: 0;
    width: 210px;
    height: 236px;
    overflow: visible;
  }
  .label__content {
    position: absolute;
    inset: 0;
    display: flex;
    flex-direction: column;
    align-items: center;
    padding-top: 38px;
    text-align: center;
  }
  .brand {
    display: flex;
    align-items: center;
    gap: 4px;
    height: 22px;
    font-size: 9px;
    font-weight: 300;
    letter-spacing: 0.4px;
    color: var(--ink-soft);
  }
  .brand__mark {
    width: 8px;
    height: 8px;
    border-radius: 50%;
    background: var(--ink-soft);
  }
  .label__name {
    margin-top: 14px;
    font-size: 40px;
    font-weight: 300;
    letter-spacing: -0.5px;
    line-height: 1;
    white-space: nowrap;
    color: var(--ink);
  }
  .label__specs {
    margin-top: 12px;
    font-size: 12px;
    font-weight: 300;
    line-height: 20px;
    color: #3a3a3a;
  }
  .ingredients {
    width: 206px;
    height: 102px;
    margin: 34px auto 0;
  }
  .ingredients--chai {
    background:
      radial-gradient(ellipse 60% 70% at 60% 45%, var(--chai-spice-a) 0%, rgba(122,68,36,0) 100%),
      linear-gradient(to bottom, rgba(236,236,236,0) 0%, var(--chai-spice-b) 55%, var(--chai-spice-a) 100%);
  }
  .ingredients--mint {
    background:
      radial-gradient(ellipse 50% 70% at 30% 60%, var(--mint-leaf-a) 0%, rgba(63,143,47,0) 100%),
      radial-gradient(ellipse 35% 55% at 85% 35%, #b7dc55 0%, rgba(183,220,85,0) 100%),
      linear-gradient(to bottom, rgba(236,236,236,0) 0%, var(--mint-leaf-b) 60%, var(--mint-leaf-a) 100%);
  }
  .ingredients--lychee {
    background:
      radial-gradient(ellipse 35% 50% at 22% 35%, var(--lychee-fruit-a) 0%, rgba(200,86,78,0) 100%),
      radial-gradient(ellipse 45% 60% at 78% 60%, var(--lychee-fruit-b) 0%, rgba(217,154,62,0) 100%),
      linear-gradient(to bottom, rgba(236,236,236,0) 0%, #dcb48a 60%, #c98a55 100%);
  }
</style>
</head>
<body>
<main class="label-set">

  <section class="label-unit label-unit--chai">
    <div class="label">
      <svg class="label__shape" viewBox="0 0 210 236" aria-hidden="true">
        <path d="M0,40 Q105,-16 210,40 Q215,118 210,196 Q105,252 0,196 Q-5,118 0,40 Z" fill="var(--chai-edge)"/>
        <path d="M2,48 Q105,-6 208,48 Q212,118 208,188 Q105,242 2,188 Q-2,118 2,48 Z" fill="var(--chai-rim)"/>
        <path d="M3,53 Q105,1 207,53 Q211,118 207,183 Q105,235 3,183 Q-1,118 3,53 Z" fill="var(--chai-fill)"/>
      </svg>
      <div class="label__content">
        <div class="brand"><span class="brand__mark"></span>Tovelin Spirits</div>
        <h2 class="label__name">Borvelle</h2>
        <p class="label__specs">Open &amp; Serve<br>12% ALC/VOL<br>750 ml</p>
      </div>
    </div>
    <div class="ingredients ingredients--chai" role="img" aria-label="Chai spices: cinnamon sticks, star anise and cloves"></div>
  </section>

  <section class="label-unit label-unit--mint">
    <div class="label">
      <svg class="label__shape" viewBox="0 0 210 236" aria-hidden="true">
        <path d="M0,40 Q105,-16 210,40 Q215,118 210,196 Q105,252 0,196 Q-5,118 0,40 Z" fill="var(--mint-edge)"/>
        <path d="M2,48 Q105,-6 208,48 Q212,118 208,188 Q105,242 2,188 Q-2,118 2,48 Z" fill="var(--mint-rim)"/>
        <path d="M3,53 Q105,1 207,53 Q211,118 207,183 Q105,235 3,183 Q-1,118 3,53 Z" fill="var(--mint-fill)"/>
      </svg>
      <div class="label__content">
        <div class="brand"><span class="brand__mark"></span>Tovelin Spirits</div>
        <h2 class="label__name">Faluntera</h2>
        <p class="label__specs">Open &amp; Serve<br>12% ALC/VOL<br>750 ml</p>
      </div>
    </div>
    <div class="ingredients ingredients--mint" role="img" aria-label="Fresh mint leaves, lime halves and green chili"></div>
  </section>

  <section class="label-unit label-unit--lychee">
    <div class="label">
      <svg class="label__shape" viewBox="0 0 210 236" aria-hidden="true">
        <path d="M0,40 Q105,-16 210,40 Q215,118 210,196 Q105,252 0,196 Q-5,118 0,40 Z" fill="var(--lychee-edge)"/>
        <path d="M2,48 Q105,-6 208,48 Q212,118 208,188 Q105,242 2,188 Q-2,118 2,48 Z" fill="var(--lychee-rim)"/>
        <path d="M3,53 Q105,1 207,53 Q211,118 207,183 Q105,235 3,183 Q-1,118 3,53 Z" fill="var(--lychee-fill)"/>
      </svg>
      <div class="label__content">
        <div class="brand"><span class="brand__mark"></span>Tovelin Spirits</div>
        <h2 class="label__name">Pomadrine</h2>
        <p class="label__specs">Open &amp; Serve<br>12% ALC/VOL<br>750 ml</p>
      </div>
    </div>
    <div class="ingredients ingredients--lychee" role="img" aria-label="Lychee fruit, ginger root and a bowl of honey"></div>
  </section>

</main>
</body>
</html>
```